Olive Oil label for bottle 0.5l approx. 10x12 cm

I am running a Spa hotel in Bavaria (logo attached) and my family lives in Greece (Bavarian and Greek flag have the same colors). They produce organic olive oil first cold pressed extra virgin. I would need a label for 0,5 liter bottles to reach them out to my guests and they should see the high quality of the olive oil and the family connection Spa-hotel Bavaria to family in Greece. The name of the family is Morvatek, the hotel is called Tannegg, the olive oil comes from Greece/Argolis/Kranidi. The name of the small olive company is Kerano Hawks. There should be a space for the best before date and the organic control number (handwritten) . The hotel logo is not mandatory. Should look nice 😉

```html
<!DOCTYPE html>
<html lang="de">
<head>
<meta charset="utf-8">
<title>Bio Olivenöl – Etikett</title>
<link rel="stylesheet" href="https://fonts.googleapis.com/css2?family=Cinzel:wght@400&family=Montserrat:wght@400;500;700&display=swap">
<style>
  :root {
    --flag-blue: #1a96d6;
    --flag-white: #ffffff;
    --slate: #5c6a66;
    --slate-soft: #7b8783;
    --organic-green: #9bc93c;
    --badge-gold: #9a8437;
    --paper: #ffffff;
  }
  * { margin: 0; padding: 0; box-sizing: border-box; }
  html, body { width: 1000px; height: 1200px; overflow: hidden; background: var(--paper); }
  .label {
    position: relative; width: 1000px; height: 1200px; background: var(--paper);
    font-family: "Montserrat", sans-serif; color: var(--slate);
  }
  .band {
    position: absolute; left: 0; width: 1000px;
    background: repeating-linear-gradient(to bottom,
      var(--flag-blue) 0 19px, var(--flag-white) 19px 34px);
  }
  .band--top { top: 0; height: 142px; }
  .band--bottom { bottom: 0; height: 144px; }
  .band__corner { position: absolute; top: 0; height: 100%; width: 200px; }
  .band__corner--left { left: 0; }
  .band__corner--right { right: 0; }
  .frame-line {
    position: absolute; top: 142px; width: 3px; height: 916px; background: var(--flag-blue);
  }
  .frame-line--left { left: 14px; }
  .frame-line--right { right: 14px; }
  .centered { position: absolute; left: 0; width: 1000px; text-align: center; }
  .hotel-name {
    top: 278px; font-size: 64px; font-weight: 500; color: var(--slate); letter-spacing: 2px;
  }
  .bio { top: 436px; font-size: 32px; letter-spacing: 8px; color: var(--slate); }
  .product {
    top: 485px; font-family: "Cinzel", serif; font-size: 124px; line-height: 1;
    color: var(--flag-blue); letter-spacing: 2px;
  }
  .variety { top: 628px; font-size: 19px; color: var(--flag-blue); letter-spacing: 0.4px; }
  .quality { top: 676px; font-size: 35px; color: var(--slate); letter-spacing: 1.5px; }
  .producer { top: 740px; font-size: 19px; font-weight: 700; letter-spacing: 2px; }
  .origin { top: 774px; font-size: 19px; letter-spacing: 2px; }
  .origin strong { font-weight: 700; }
  .field-label { position: absolute; font-size: 20px; color: var(--slate); letter-spacing: 1px; }
  .field-label--date { left: 34px; top: 927px; }
  .field-label--family { left: 416px; top: 915px; width: 200px; text-align: center; letter-spacing: 2px; }
  .field-label--control { left: 745px; top: 927px; width: 218px; text-align: center; }
  .write-box { position: absolute; top: 964px; height: 60px; border: 1.5px solid #8a9491; background: var(--paper); }
  .write-box--date { left: 36px; width: 254px; }
  .write-box--control { left: 745px; width: 218px; }
  .family-signature {
    position: absolute; left: 310px; top: 954px; width: 420px; height: 72px;
    background: linear-gradient(90deg, #eef1f0, #dde2e0, #eef1f0); border-radius: 6px;
  }
  .seal { position: absolute; }
  .seal--inspection {
    left: 320px; top: 1060px; width: 136px; height: 136px; border-radius: 50%;
    background: var(--badge-gold);
  }
  .seal--organic { left: 484px; top: 1077px; width: 184px; height: 102px; background: var(--organic-green); }
</style>
</head>
<body>
<main class="label">
  <div class="band band--top">
    <svg class="band__corner band__corner--left" viewBox="0 0 200 142" role="img" aria-label="Bavarian lozenge pattern">
      <polygon points="0,0 200,0 90,142 0,142" fill="#8fcaea"/>
    </svg>
    <svg class="band__corner band__corner--right" viewBox="0 0 200 142" role="img" aria-label="Bavarian lozenge pattern">
      <polygon points="0,0 200,0 200,142 110,142" fill="#8fcaea"/>
    </svg>
  </div>
  <div class="frame-line frame-line--left"></div>
  <div class="frame-line frame-line--right"></div>

  <div class="centered hotel-name">Tannegg</div>

  <div class="centered bio">BIO</div>
  <h1 class="centered product">OLIVENÖL</h1>
  <p class="centered variety">Sortenreine Manaki-Oliven aus kontrolliert biologischen Anbau</p>
  <p class="centered quality">kaltextrahiert | nativ extra | ungefiltert</p>
  <p class="centered producer">by Kerano Hawks</p>
  <p class="centered origin"><strong>produziert in</strong> Kranidi, Argolis, Griechenland</p>

  <span class="field-label field-label--date">mindestens haltbar bis:</span>
  <div class="write-box write-box--date"></div>
  <span class="field-label field-label--family">Familie</span>
  <div class="family-signature" role="img" aria-label="Handwritten family name Morvatek-Delkarou"></div>
  <span class="field-label field-label--control">Kontrollnumm</span>
  <div class="write-box write-box--control"></div>

  <div class="band band--bottom">
    <svg class="band__corner band__corner--left" viewBox="0 0 200 144" role="img" aria-label="Bavarian lozenge pattern">
      <polygon points="0,0 90,0 200,144 0,144" fill="#8fcaea"/>
    </svg>
    <svg class="band__corner band__corner--right" viewBox="0 0 200 144" role="img" aria-label="Bavarian lozenge pattern">
      <polygon points="110,0 200,0 200,144 0,144" fill="#8fcaea"/>
    </svg>
  </div>
  <div class="seal seal--inspection" role="img" aria-label="Organic inspection certificate"></div>
  <div class="seal seal--organic" role="img" aria-label="Organic farming certificate"></div>
</main>
</body>
</html>
```